Flyer Design

I will be hosting an event at Penrith's bright margin. Here is a link to their page http://www.thebrightmargin.com.au/events-and-workshops/whats-on-penrith/. I have attached the details of my course from their website below. I hope this is of some valuable assistance.

Florist and lover of all things gorgeous, Marla Hutchin from Marla Hutchin Flowers will be running this beautiful and fun workshop. Come along to learn how to make your very own floral crown. All you need to bring are some closed in shoes, an apron and an open mind ready for creativity!

Teens & adults welcome

Date 1: Saturday 11 April 2015
Time 1: 11:00-2:00pm

Date 2: Thursday 23 April 2015
Time 2: 6:00-9:00pm

Cost: $90 per person (includes materials provided – see list below)
Place: The Bright Margin, Unit 3, 87 Tolland Street Penrith
RSVP: Marla via email marlahutchinflowers@mailbox-demo.net or phone 0491 357 206

Materials provided:
• Florist scissors
• Parafilm
• Wire
• Flowers
• light snacks & refreshments

```html
<!DOCTYPE html>
<html lang="en">
<head>
<meta charset="utf-8">
<title>Floral Crowns Workshop Flyer</title>
<link rel="stylesheet" href="https://fonts.googleapis.com/css2?family=Pinyon+Script&family=Cabin:wght@400;500;600&family=Lato:wght@400&display=swap">
<style>
  :root {
    --page-bg: #f4f4f4;
    --plum: #4f3d6b;
    --plum-mid: #5b4877;
    --mauve: #8b6b9f;
    --cocoa: #4a3f40;
    --pink: #c65a9f;
    --pink-soft: #f0b8e0;
    --lilac: #e4dcee;
    --ink: #2a2836;
    --label: #f2e35a;
    --white: #ffffff;
    --title: #e9e6e6;
  }
  * { margin: 0; padding: 0; box-sizing: border-box; }
  html, body { width: 1200px; height: 900px; overflow: hidden; background: var(--page-bg); }
  .flyer {
    position: absolute; left: 330px; top: 12px; width: 590px; height: 833px;
    overflow: hidden; background: var(--lilac);
    box-shadow: 0 4px 18px rgba(0,0,0,.18);
    font-family: "Cabin", sans-serif; color: var(--ink);
  }
  .flyer > * { position: absolute; }
  .backdrop { left: 0; top: 0; width: 590px; height: 833px; }
  .hero-photo {
    left: 330px; top: 36px; width: 260px; height: 340px;
    background: radial-gradient(circle at 45% 40%, #f3e3df 0%, #d9c3bd 35%, #a9b08e 75%, #7f8a63 100%);
  }
  .flower-photo {
    left: 0; top: 345px; width: 210px; height: 488px;
    background: radial-gradient(ellipse 80% 60% at 35% 55%, #eef0cf 0%, #c3d47c 35%, #6e9444 65%, rgba(228,220,238,0) 100%);
  }
  .title-script {
    left: 16px; top: 88px; font-family: "Pinyon Script", cursive; font-size: 66px;
    color: var(--title); line-height: 1; text-shadow: 1px 2px 3px rgba(0,0,0,.5);
  }
  .title-word {
    left: 24px; top: 162px; font-family: "Lato", sans-serif; font-size: 44px; line-height: 1.1;
    letter-spacing: 9px; color: var(--title); text-shadow: 1px 2px 3px rgba(0,0,0,.5);
  }
  .tagline {
    left: 18px; top: 272px; font-family: "Pinyon Script", cursive; font-size: 27px;
    color: var(--white); transform: rotate(-8.5deg); transform-origin: left center; white-space: nowrap;
  }
  .badge { left: 445px; top: 240px; width: 140px; height: 140px; }
  .intro {
    left: 100px; top: 365px; width: 440px; text-align: center;
    font-size: 17px; line-height: 23px; white-space: nowrap;
  }
  .come-along {
    left: 180px; top: 418px; width: 410px; height: 54px; padding: 3px 0 0 38px;
    color: var(--white); font-size: 17px; line-height: 22px; white-space: nowrap;
  }
  .come-along strong { font-weight: 400; font-size: 24px; color: var(--pink-soft); }
  .come-along em { font-style: italic; }
  .bring {
    left: 193px; top: 478px; font-size: 17.5px; line-height: 24px; white-space: nowrap;
  }
  .materials-heading {
    left: 200px; top: 545px; font-size: 17px; font-weight: 600; color: var(--pink);
    text-decoration: underline; letter-spacing: .5px;
  }
  .materials { left: 198px; top: 576px; list-style: none; font-size: 18px; line-height: 26px; }
  .materials li { height: 33px; }
  .materials li::before { content: "• "; }
  .session {
    width: 128px; height: 128px; border-radius: 50%; background: var(--plum);
    border: 3px solid var(--white); box-shadow: 5px 4px 0 var(--plum-mid);
    color: var(--white); text-align: center; padding-top: 20px;
    font-size: 14px; font-weight: 600; line-height: 19px; white-space: nowrap;
  }
  .session .label { color: var(--label); font-size: 11px; font-weight: 400; text-decoration: underline; line-height: 14px; }
  .session-one { left: 404px; top: 530px; }
  .session-two { left: 452px; top: 643px; }
  .details {
    left: 0; top: 768px; width: 590px; text-align: center; color: var(--white);
    font-size: 13px; line-height: 17px; white-space: nowrap;
  }
  .details .label { color: var(--label); }
</style>
</head>
<body>
<main class="flyer">
  <svg class="backdrop" viewBox="0 0 590 833" aria-hidden="true">
    <defs>
      <linearGradient id="lilacFade" x1="0" y1="0" x2="0" y2="1">
        <stop offset="0" stop-color="#cfc3df"/><stop offset="1" stop-color="#ece6f3"/>
      </linearGradient>
    </defs>
    <rect width="590" height="833" fill="url(#lilacFade)"/>
    <rect width="590" height="40" fill="var(--plum)"/>
    <path d="M0 28 Q295 52 590 30 L590 42 Q295 62 0 40Z" fill="var(--white)"/>
  </svg>

  <div class="hero-photo" role="img" aria-label="Photo of a young woman wearing a pink floral crown"></div>

  <svg class="backdrop" viewBox="0 0 590 833" aria-hidden="true">
    <path d="M0 40 Q295 62 330 52 L410 330 L402 355 L0 345Z" fill="var(--cocoa)"/>
    <path d="M0 345 L150 326 L300 320 L402 356 Q500 370 590 352 L590 372 Q470 392 402 370 L300 336 L0 360Z" fill="var(--white)" opacity=".9"/>
    <polygon points="0,290 378,220 392,250 370,262 0,335" fill="var(--pink)"/>
    <polygon points="378,220 400,245 392,250" fill="#8e3c72"/>
  </svg>

  <div class="flower-photo" role="img" aria-label="Photo of a bouquet of white roses and green blossoms"></div>

  <div class="title-script">Floral Crowns</div>
  <div class="title-word">WORKSHOP</div>
  <div class="tagline">Florist and lover of all things gorgeous</div>

  <svg class="badge" viewBox="0 0 140 140" aria-label="Teens and adults welcome">
    <polygon fill="var(--plum-mid)" points="70,4 80,22 99,12 101,33 122,31 114,51 133,60 117,73 131,89 110,93 114,114 94,109 88,130 72,117 58,133 50,113 30,120 32,99 11,96 23,79 6,67 24,56 14,37 35,37 36,16 55,24"/>
    <polygon fill="#dcc6ea" points="70,14 78,28 94,20 96,37 113,36 106,52 122,60 109,71 121,84 103,88 106,105 90,101 85,118 72,107 61,120 54,104 38,110 39,93 22,90 32,76 18,66 33,56 25,41 42,41 43,24 58,31"/>
    <polygon fill="var(--plum)" points="36,80 122,56 120,76 110,100 60,114 30,102"/>
    <g transform="rotate(-16 70 70)" font-family="Cabin, sans-serif" font-weight="600" text-anchor="middle" fill="var(--white)">
      <text x="66" y="60" font-size="15" fill="var(--plum)">TEENS</text>
      <text x="72" y="80" font-size="15">&amp; ADULTS</text>
      <text x="74" y="99" font-size="15">WELCOME</text>
    </g>
  </svg>

  <p class="intro">Marla Hutchin from Marla Hutchin Flowers will be<br>running this beautiful and fun workshop.</p>

  <svg class="backdrop" viewBox="0 0 590 833" aria-hidden="true">
    <polygon points="180,418 590,418 590,472 210,472 195,445" fill="var(--mauve)"/>
  </svg>
  <p class="come-along"><strong>COME ALONG</strong> to learn how to make<br>your very own <em>floral crown.</em></p>

  <p class="bring">All you need to bring are some closed in shoes,<br>an apron and an open mind ready for creativity!</p>

  <h2 class="materials-heading">MATERIALS PROVIDED:</h2>
  <ul class="materials">
    <li>Florist scissors</li>
    <li>Parafilm</li>
    <li>Wire</li>
    <li>Flowers</li>
    <li>light snacks &amp; refreshments</li>
  </ul>

  <div class="session session-one">
    <div class="label">Date 1:</div>
    <div>Saturday</div>
    <div>11 April 2015</div>
    <div class="label">Time 1:</div>
    <div>11:00-2:00pm</div>
  </div>
  <div class="session session-two">
    <div class="label">Date 2:</div>
    <div>Thursday</div>
    <div>23 April 2015</div>
    <div class="label">Time 2:</div>
    <div>6:00-9:00pm</div>
  </div>

  <svg class="backdrop" viewBox="0 0 590 833" aria-hidden="true">
    <path d="M0 770 Q300 755 590 764 L590 833 L0 833Z" fill="var(--plum-mid)"/>
    <path d="M0 766 Q300 751 590 760 L590 764 Q300 755 0 770Z" fill="var(--white)"/>
  </svg>
  <div class="details">
    <div><span class="label">Cost:</span> $90 per person (includes materials provided – see list below)</div>
    <div><span class="label">Place:</span> The Bright Margin, Unit 3, 87 Tolland Street Penrith</div>
    <div><span class="label">RSVP:</span> Marla via email marlahutchinflowers@mailbox-demo.net or phone 0491 357 206</div>
  </div>
</main>
</body>
</html>
```